Bref créative
Design Business Card & Stationary
Talvix Studio
Professional
Derek Holt
4837 Birchwood Lane Suite #210
Maple Ridge, OR 97310
derek@talvixstudio.example
www.talvixstudio.example
This is our logo

```html
<!DOCTYPE html>
<html lang="en">
<head>
<meta charset="utf-8">
<title>Talvix Studio — Business Card</title>
<link href="https://fonts.googleapis.com/css2?family=Open+Sans:wght@400;600;700&display=swap" rel="stylesheet">
<style>
  :root {
    --backdrop: #2b2b2b;
    --card: #ffffff;
    --green: #8cc63f;
    --green-deep: #5a9a1e;
    --green-light: #c3e27a;
    --ink: #1d1d1d;
    --brand-ink: #3a4a3a;
  }
  html, body {
    margin: 0;
    width: 1200px;
    height: 906px;
    overflow: hidden;
    background: var(--backdrop);
    font-family: "Open Sans", Arial, sans-serif;
  }
  .business-card {
    position: absolute;
    left: 180px;
    top: 213px;
    width: 840px;
    height: 480px;
    background: var(--card);
    border-radius: 28px;
    overflow: hidden;
    box-shadow: 0 18px 40px rgba(0,0,0,0.45);
  }
  .card-swooshes {
    position: absolute;
    inset: 0;
  }
  .brand {
    position: absolute;
    left: 56px;
    top: 84px;
  }
  .brand-row {
    display: flex;
    align-items: center;
    gap: 14px;
  }
  .brand-mark {
    width: 42px;
    height: 42px;
    background: var(--brand-ink);
  }
  .brand-name {
    font-size: 50px;
    font-weight: 600;
    line-height: 1;
    color: var(--brand-ink);
    letter-spacing: -1px;
  }
  .brand-tagline {
    margin: 6px 0 0 58px;
    font-size: 14px;
    color: var(--green-deep);
    letter-spacing: 0.3px;
  }
  .holder-name {
    position: absolute;
    left: 318px;
    top: 196px;
    margin: 0;
    font-size: 30px;
    line-height: 40px;
    font-weight: 700;
    color: var(--green-deep);
  }
  .contact {
    position: absolute;
    right: 60px;
    top: 250px;
    margin: 0;
    font-style: normal;
    text-align: right;
    font-size: 19px;
    line-height: 28px;
    color: var(--ink);
  }
  .contact .email { margin-top: 12px; }
</style>
</head>
<body>
  <section class="business-card">
    <svg class="card-swooshes" viewBox="0 0 840 480" width="840" height="480" aria-hidden="true">
      <defs>
        <linearGradient id="greenBand" x1="0" y1="0" x2="1" y2="1">
          <stop offset="0" stop-color="#c3e27a"/>
          <stop offset="0.5" stop-color="#8cc63f"/>
          <stop offset="1" stop-color="#5a9a1e"/>
        </linearGradient>
      </defs>
      <path d="M430 0 H840 V150 C760 150 700 120 640 80 C590 48 520 28 430 0 Z" fill="url(#greenBand)"/>
      <path d="M520 46 C600 68 640 108 700 135 C745 155 790 160 840 158 V150 C780 156 740 148 700 128 C650 104 600 66 520 46 Z" fill="#111"/>
      <path d="M0 365 C90 350 170 380 240 420 C290 450 340 470 380 480 H0 Z" fill="url(#greenBand)"/>
      <path d="M0 352 C90 338 170 366 245 408 C295 436 340 458 380 480 H372 C330 462 290 442 240 414 C170 374 90 348 0 360 Z" fill="#111"/>
    </svg>

    <div class="brand">
      <div class="brand-row">
        <span class="brand-mark"></span>
        <span class="brand-name">Talvix Studio</span>
      </div>
      <p class="brand-tagline">Internet Presence Management</p>
    </div>

    <h1 class="holder-name">Derek Holt</h1>

    <address class="contact">
      <div>4837 Birchwood Lane Suite #210</div>
      <div>Maple Ridge, OR 97310</div>
      <div>P : 555-014-2387</div>
      <div>F : 555-014-6621</div>
      <div class="email">E : derek@talvixstudio.example</div>
      <div>www.talvixstudio.example</div>
    </address>
  </section>
</body>
</html>
```